Ecommerce brand for entrepreneurs needs help with branding products

I am looking for help to design a small supplement pouch. Including colours, layout and design.

The business:
The business is called 'Keel Orbit' and our goal is to help entrepreneurs continue to change the world in spite of how difficult it is.

At Keel Orbit, we understand being an entrepreneur is one of the hardest jobs there is. We believe there is a better way. A way in which you don’t have to choose between success in your business and the rest of your life. Our aim is to solve these challenges, so you can stay in the fight a little longer. If we can do this, we can ultimately change the world into a better place.

We will do this through a range of supplements, community, information and physical products to help you optimise their lives.

The product:
The product I am looking to create is for a natural nootropic called

‘The Velvet Compass’

The product will address the challenges with focus and lower attention spans.

So Entrepreneurs can Solve more problems, Help more people and make more money.

Do more in four hours than a whole day. Have Zen like calm. With Zero Jitters & Zero Crashes. Do what others can’t

The design:
I want this to be a small pouch. The final design should be elegant, and minimalist and have an edge that is different.

I have added examples of products that I like below.

I am open to most colour combinations but silver, navy, black, orange, white and translucent are what is taking my fancy right now.

I like the idea of having a translucent package or part of the package like some of the designs below. I also like the matt finish of some of the designs along with the flashes of shininess from silver for contrast. or even using embossing within the packaging.

I have a logo that I have made but I am open to changes on that as well if you see fit. if you do want to do this, I would love to see an emblem next to the words Keel Orbit that encapsulates the brand.

I have done some really really rough mockups myself but would like to see what you have to offer rather than what I have done

The purpose of this image:
I need a 3D mockup of this supplement to be on my landing page to start to take pre-orders.

I am ideally looking for 2 images

1) Supplement packaging on its own
2) Supplement packaging with background coloured lighting, with powder on the ground etc

Need extra days to review

Target Market(s)

The logo: Please also redesign my logo - I would love to see an emblem next to the words Keel Orbit that encapsulates the brand.The business is called 'Keel Orbit' and our goal is to help entrepreneurs continue to change the world in spite of how difficult it is. At Keel Orbit, we understand being an entrepreneur is one of the hardest jobs there is. We believe there is a better way. A way in which you don’t have to choose between success in your business and the rest of your life. Our aim is to solve these challenges, so you can stay in the fight a little longer. If we can do this, we can ultimately change the world into a better place. We will do this through a range of supplements, community, information and physical products to help you optimise their lives.

Industry/Entity Type

Supplements for entrepreneurs

Colors

Requirements
Must have
• The design: I want this to be a small pouch. The final design should be elegant, and minimalist and have an edge that is different. I have added examples of products that I like below. I am open to most colour combinations but silver, navy, black, orange, white and translucent are what is taking my fancy right now. I like the idea of having a translucent package or part of the package like some of the designs below. I also like the matt finish of some of the designs along with the flashes of shininess from silver for contrast. or even using embossing within the packaging.

```html
<!DOCTYPE html>
<html lang="en">
<head>
<meta charset="utf-8">
<title>Keel Orbit – Natural Nootropic Pouch</title>
<link rel="stylesheet" href="https://fonts.googleapis.com/css2?family=Montserrat:wght@300;500;800&display=swap">
<style>
  :root {
    --backdrop: #959595;
    --pouch-black: #0b0b0b;
    --pouch-edge: #1c1c1c;
    --band-top: #c8345f;
    --band-mid: #dd6a48;
    --band-bottom: #e2901f;
    --ink-dark: #141414;
    --ink-light: #f2f2f2;
  }
  * { margin: 0; padding: 0; box-sizing: border-box; }
  html, body {
    width: 1200px;
    height: 800px;
    overflow: hidden;
    background: var(--backdrop);
    font-family: "Montserrat", sans-serif;
  }
  .canvas {
    position: relative;
    width: 1200px;
    height: 800px;
  }
  .pouch {
    position: absolute;
    left: 392px;
    top: 82px;
    width: 410px;
    height: 648px;
    background: var(--pouch-black);
    border-radius: 18px 18px 30px 30px;
    overflow: hidden;
  }
  .pouch__notch {
    position: absolute;
    top: 42px;
    width: 8px;
    height: 6px;
    border-radius: 50%;
    background: var(--backdrop);
  }
  .pouch__notch--left { left: -4px; }
  .pouch__notch--right { right: -4px; }
  .pouch__zip {
    position: absolute;
    left: 18px;
    right: 18px;
    top: 82px;
    height: 2px;
    background: var(--pouch-edge);
  }
  .pouch__zip--lower { top: 88px; }
  .label-band {
    position: absolute;
    left: 102px;
    top: 0;
    width: 203px;
    height: 436px;
    background: linear-gradient(180deg, var(--band-top) 0%, var(--band-mid) 45%, var(--band-bottom) 100%);
  }
  .label-band__category {
    position: absolute;
    top: 32px;
    width: 100%;
    text-align: center;
    font-size: 10.5px;
    font-weight: 500;
    letter-spacing: 3px;
    color: var(--ink-dark);
  }
  .brand {
    position: absolute;
    left: 0;
    right: 0;
    top: 390px;
    display: flex;
    align-items: center;
    justify-content: center;
    gap: 8px;
  }
  .brand__dot {
    width: 12px;
    height: 12px;
    border-radius: 50%;
    background: var(--ink-dark);
  }
  .brand__name {
    font-size: 19px;
    font-weight: 800;
    letter-spacing: 4px;
    color: var(--ink-dark);
    text-transform: uppercase;
  }
  .tagline {
    position: absolute;
    left: 0;
    right: 0;
    top: 488px;
    text-align: center;
    font-size: 19px;
    font-weight: 300;
    letter-spacing: 7px;
    line-height: 1.2;
    color: var(--ink-light);
    text-transform: uppercase;
  }
</style>
</head>
<body>
  <main class="canvas">
    <section class="pouch">
      <span class="pouch__notch pouch__notch--left"></span>
      <span class="pouch__notch pouch__notch--right"></span>
      <div class="label-band">
        <p class="label-band__category">NATURAL NOOTROPIC</p>
        <div class="brand">
          <span class="brand__dot"></span>
          <span class="brand__name">Keel Orbit</span>
        </div>
      </div>
      <span class="pouch__zip"></span>
      <span class="pouch__zip pouch__zip--lower"></span>
      <p class="tagline">The Velvet<br>Compass</p>
    </section>
  </main>
</body>
</html>
```